Business Cards for our company

Hi there,

we have successfully designed a logo with ArtFlock and would like now to design our business cards. We would like to keep the colours and the look-and-feel of the logo. Please send in variations with two or three colours and one or two sides. I promise to respond to every single submission.

Many thanks and happy new year.

All the best,
Wilfried

Target Market(s)

B2B

Industry/Entity Type

Trade

Contact Information for Business Card

We have successfully designed a logo with ArtFlock and would like now to design our business cards. We would like to keep the colours and the look-and-feel of the logo. Please send in variations with two or three colours and one or two sides. I promise to respond to every single submission.

Font styles to use
Serif
Sans Serif
Script

Requirements
Must have
• These information should be on the business card, grouped as you suggest, and we think using small pictograms for mobile, email, etc is pretty helpful:
• Wilfried Tammler (first and second name)
• Geschäftsführer/ Managing Director (title)
• KoR Warenkontor GmbH (company name and legal form)
• Ostheimer Str. 18/3 (street and house number)
• 71384 Kleinwarden (zip code and town)
• +491709384562 (mobile)
• +4955509027341 (work)
• w.tammler@kor-warenkontor.example (email)
• www.kor-warenkontor.example (web)
Nice to have
• Spectacular and interesting layout and design. You look at it and think, wow, that's not the normal stuff.
• We think of ourselves as bridge-builders between businesses (international producers on the one hand, and retail chains on the other hand) and we translate, organise and manage projects where both partners are involved, but it's difficult for them to cooperate due to language barriers and different working cultures.
• This is why we have the n between the B's shaped as a bridge, and the green arc supports this idea. Maybe you could play with this idea...
Should not have
• the standard layout that everybody has

```html
<!DOCTYPE html>
<html lang="de">
<head>
<meta charset="utf-8">
<title>KoR Warenkontor – Visitenkarten</title>
<link rel="stylesheet" href="https://fonts.googleapis.com/css2?family=Cinzel:wght@400&family=Montserrat:wght@400;700&display=swap">
<style>
  :root {
    --stage: #1c1c1d;
    --card: #0b0b0c;
    --white: #ffffff;
    --text: #e6e6e6;
    --silver: #b9b9b9;
    --green: #2fb54a;
  }
  * { margin: 0; padding: 0; box-sizing: border-box; }
  html, body { width: 1200px; height: 900px; overflow: hidden; background: var(--stage); }
  .canvas { position: relative; width: 1200px; height: 900px; }

  .card {
    position: absolute;
    width: 760px;
    height: 420px;
    background: var(--card);
    box-shadow: 0 18px 40px rgba(0,0,0,.55);
    font-family: "Montserrat", sans-serif;
    color: var(--text);
  }
  .card--front { left: 110px; top: 40px; }
  .card--back { left: 330px; top: 445px; }

  .front-company {
    position: absolute;
    top: 150px; right: 70px;
    font-weight: 700;
    font-size: 19px;
    letter-spacing: 4px;
    color: var(--white);
  }
  .front-wordmark {
    position: absolute;
    left: 60px; top: 205px;
    display: flex; align-items: center; gap: 16px;
  }
  .wordmark-dot { width: 14px; height: 14px; border-radius: 50%; background: var(--silver); }
  .front-wordmark .wordmark-name {
    font-weight: 700; font-size: 46px; color: var(--silver); letter-spacing: 1px;
  }

  .back-wordmark {
    position: absolute;
    right: 50px; top: 80px;
    display: flex; align-items: center; gap: 14px;
  }
  .wordmark-square { width: 14px; height: 14px; background: var(--green); }
  .back-wordmark .wordmark-name {
    font-weight: 700; font-size: 46px; color: var(--white); letter-spacing: 1px;
  }

  .contact {
    position: absolute;
    left: 40px; bottom: 40px;
    padding-left: 22px;
    border-left: 8px solid var(--green);
  }
  .contact-name {
    font-family: "Cinzel", serif;
    font-size: 25px;
    letter-spacing: 4px;
    color: var(--white);
    line-height: 1.1;
  }
  .contact-title { color: var(--green); font-size: 16px; margin-bottom: 6px; }
  .contact-line { font-size: 16px; line-height: 23px; display: flex; align-items: center; gap: 10px; }
  .contact-line svg { width: 12px; height: 12px; flex: none; fill: none; stroke: var(--green); stroke-width: 2; }
  .contact-address { margin-bottom: 2px; }
</style>
</head>
<body>
<div class="canvas">

  <section class="card card--front">
    <div class="front-company">KOR WARENKONTOR GMBH</div>
    <div class="front-wordmark">
      <span class="wordmark-dot"></span>
      <span class="wordmark-name">KoR Warenkontor</span>
    </div>
  </section>

  <section class="card card--back">
    <div class="back-wordmark">
      <span class="wordmark-square"></span>
      <span class="wordmark-name">KoR Warenkontor</span>
    </div>

    <div class="contact">
      <div class="contact-name">WILFRIED TAMMLER</div>
      <div class="contact-title">Geschäftsführer/ Managing Director</div>
      <div class="contact-address">
        <div class="contact-line">Ostheimer Str. 18/3</div>
        <div class="contact-line">71384 Kleinwarden</div>
      </div>
      <div class="contact-line">
        <svg viewBox="0 0 12 12" aria-hidden="true"><rect x="3" y="1" width="6" height="10" rx="1"/></svg>
        +491709384562
      </div>
      <div class="contact-line">
        <svg viewBox="0 0 12 12" aria-hidden="true"><path d="M2 1.5l2.5 0 1 2.5-1.5 1a6 6 0 0 0 3 3l1-1.5 2.5 1v2.5c-5 0-8.5-3.5-8.5-8.5z"/></svg>
        +4955509027341
      </div>
      <div class="contact-line">
        <svg viewBox="0 0 12 12" aria-hidden="true"><rect x="1" y="2.5" width="10" height="7"/><path d="M1 2.5l5 4 5-4"/></svg>
        w.tammler@kor-warenkontor.example
      </div>
      <div class="contact-line">
        <svg viewBox="0 0 12 12" aria-hidden="true"><circle cx="6" cy="6" r="5"/><path d="M1 6h10M6 1c-2.5 3-2.5 7 0 10M6 1c2.5 3 2.5 7 0 10"/></svg>
        www.kor-warenkontor.example
      </div>
    </div>
  </section>

</div>
</body>
</html>
```